VELORA Group Fitness Class Launch Poster!

We need a poster design for a upcoming Group Fitness Class launch with two additional social media post designs.
Please follow our Brand Style Guide, as I will not be able to accept anything outside of this guide.
Class Description:
Come and VELORA your body with this class while catching up with friends and meeting new people. It is low-impact strength training with bodyweight exercises to help improve muscular strength, cardiovascular endurance, balance, bone health and functional training. It is suitable for all fitness levels.
Class Length: 30 Minutes
Intro script for class online:
📣New class alert❗
TPW team is excited to announce the launch of our new class, "VELORA", instructed by Jo! 🥰
Unsure if group fitness classes are for you? Join us for 30-minute low-impact strength training with bodyweight exercises! It's time to build your confidence in a fun and supportive environment.
Target Market(s)
Target audience is mostly females which barrier to entry to fitness is not having the confidence to join or has limited capability and needing low impact. Important to note that our demographic tends to be below 50... So barriers is most likely to be confidence, overweight or unfit.
Industry/Entity Type
Fitness
Other font styles liked:
- Please follow the Style Guide Fonts.
Requirements
Must have
- The project must follow our Brand Guidelines & include the class logo. Poster should be exciting and stand out. Don't necessarily have to use the stock images provided.
Should not have
- If you select your own image, the preference would be that it does not only include slim/fit looking individuals.

```html
<!DOCTYPE html>
<html lang="en">
<head>
<meta charset="utf-8">
<title>VELORA – New Class Poster</title>
<link rel="stylesheet" href="https://fonts.googleapis.com/css2?family=Fredoka:wght@500;600;700&family=Rubik:wght@800;900&family=Roboto:wght@400;500&display=swap">
<style>
  :root {
    --page: #ecebe8;
    --red: #a81c32;
    --red-light: #bf3a4e;
    --white: #ffffff;
    --grey-band: #e6e6ea;
    --ink: #222226;
    --wedge: #2a2a2a;
  }
  * { box-sizing: border-box; margin: 0; padding: 0; }
  html, body { width: 1200px; height: 2740px; overflow: hidden; background: var(--page); }
  .poster {
    position: absolute; left: 50px; top: 590px; width: 1100px; height: 1559px;
    overflow: hidden; box-shadow: 0 10px 30px rgba(0,0,0,.25); background: var(--red);
    font-family: "Roboto", Arial, sans-serif; color: var(--white);
  }
  .poster-bg { position: absolute; inset: 0; }
  .abs { position: absolute; }
  .class-mark {
    left: 0; right: 0; top: 46px; text-align: center;
    font-family: "Rubik", "Fredoka", Arial, sans-serif; font-weight: 900; font-size: 92px; line-height: 1.1;
    color: var(--white); letter-spacing: 2px;
  }
  .headline {
    left: 0; right: 0; top: 764px; text-align: center;
    font-family: "Rubik", "Fredoka", Arial, sans-serif; font-weight: 900; font-size: 74px; line-height: 1; letter-spacing: 1px;
  }
  .sub-online {
    left: 0; right: 0; top: 850px; text-align: center;
    font-family: "Fredoka", Arial, sans-serif; font-weight: 600; font-size: 23px; line-height: 1; letter-spacing: 9px;
  }
  .announce {
    left: 51px; width: 996px; top: 891px; height: 47px; background: var(--grey-band);
    color: var(--ink); text-align: center; font-family: "Fredoka", Arial, sans-serif; font-weight: 600;
    font-size: 27px; line-height: 47px; white-space: nowrap;
  }
  .announce .team { color: var(--red); }
  .class-name {
    left: 118px; top: 990px; display: flex; align-items: center; gap: 14px;
    font-family: "Fredoka", Arial, sans-serif; font-weight: 700; font-size: 60px; line-height: 1;
  }
  .class-name .dot { width: 26px; height: 26px; border-radius: 50%; background: var(--white); }
  .instructor {
    left: 117px; top: 1055px; width: 335px; height: 46px; border-radius: 23px; background: var(--ink);
    text-align: center; font-family: "Fredoka", Arial, sans-serif; font-weight: 500; font-size: 28px; line-height: 46px;
  }
  .length { left: 120px; top: 1108px; display: flex; align-items: center; gap: 10px; }
  .length .num { font-family: "Fredoka", Arial, sans-serif; font-weight: 700; font-size: 72px; line-height: 1; }
  .length .label { font-family: "Fredoka", Arial, sans-serif; font-weight: 600; font-size: 28px; line-height: 1; }
  .length .unit { font-family: "Fredoka", Arial, sans-serif; font-weight: 600; font-size: 21px; letter-spacing: 7px; margin-top: 6px;
    border-bottom: 2px solid var(--ink); padding-bottom: 4px; }
  .question {
    left: 560px; top: 995px; font-family: "Fredoka", Arial, sans-serif; font-weight: 600; font-size: 31px; line-height: 1.05;
  }
  .question span { display: inline-block; border-bottom: 4px solid var(--ink); }
  .invite {
    left: 560px; top: 1075px; width: 487px; height: 110px; border: 2px solid var(--white);
    border-bottom: 8px solid var(--ink); border-radius: 4px; padding: 12px 16px;
    font-size: 18px; line-height: 1.2;
  }
  .invite strong { font-weight: 500; }
  .info-box {
    left: 51px; width: 996px; border: 2px solid rgba(255,255,255,.6); border-radius: 4px; text-align: center;
    font-size: 21px; line-height: 1.3;
  }
  .info-box .tab {
    position: absolute; left: 50%; top: -2px; transform: translateX(-50%); width: 660px; height: 38px;
    clip-path: polygon(6% 0, 100% 0, 94% 100%, 0 100%); background: var(--white); color: var(--red);
    font-family: "Fredoka", Arial, sans-serif; font-weight: 600; font-size: 30px; line-height: 38px; letter-spacing: 1px;
    text-align: center; white-space: nowrap;
  }
  .info-box p { position: absolute; left: 100px; right: 100px; white-space: nowrap; }
  .figure { position: absolute; height: 56px; border-radius: 6px; background: var(--red-light); }
  .box-together { top: 1229px; height: 118px; }
  .box-together p { top: 48px; }
  .box-strength { top: 1366px; height: 150px; }
  .box-strength p { top: 46px; }
</style>
</head>
<body>
  <div class="poster">
    <svg class="poster-bg" width="1100" height="1559" viewBox="0 0 1100 1559">
      <defs>
        <linearGradient id="gym" x1="0" y1="0" x2="1" y2="1">
          <stop offset="0" stop-color="#3d454d"/>
          <stop offset="1" stop-color="#22272b"/>
        </linearGradient>
      </defs>
      <rect width="1100" height="760" fill="url(#gym)" role="img" aria-label="Photo: group of women and men doing bodyweight lunges in a gym"/>
      <path d="M0 610 L330 560 L0 726 Z" fill="var(--wedge)"/>
      <path d="M640 560 C820 560 980 600 1100 640 L1100 728 C900 600 750 580 640 585 Z" fill="var(--white)"/>
      <path d="M0 726 C250 600 700 560 1100 728 L1100 1559 L0 1559 Z" fill="var(--red)"/>
      <circle cx="392" cy="592" r="162" fill="none" stroke="rgba(255,255,255,.18)" stroke-width="10"/>
      <circle cx="705" cy="592" r="162" fill="none" stroke="rgba(255,255,255,.18)" stroke-width="10"/>
      <circle cx="392" cy="592" r="146" fill="#3a4147" stroke="var(--white)" stroke-width="6" role="img" aria-label="Photo: two people doing squats"/>
      <circle cx="705" cy="592" r="146" fill="#343a40" stroke="var(--white)" stroke-width="6" role="img" aria-label="Photo: woman doing sit-ups on a mat"/>
    </svg>

    <div class="abs class-mark">VELORA</div>

    <div class="abs headline">NEW CLASS ALERT</div>
    <div class="abs sub-online">CLASS ONLINE</div>
    <div class="abs announce"><span class="team">TPW TEAM</span> IS EXCITED TO ANNOUNCE THE LAUNCH OF OUR NEW CLASS</div>

    <div class="abs class-name"><span class="dot"></span>VELORA</div>
    <div class="abs instructor">INSTRUCTED BY JO!</div>
    <div class="abs length">
      <div class="num">30</div>
      <div><div class="label">CLASS LENGTH</div><div class="unit">MINUTES</div></div>
    </div>

    <div class="abs question"><span>UNSURE IF GROUP FITNESS</span><br><span>CLASSES ARE FOR YOU?</span></div>
    <div class="abs invite"><strong>Join us for 30-minute low-impact strength training</strong> with bodyweight exercises! It's time to build your confidence in a fun &amp; supportive environment.</div>

    <div class="abs info-box box-together">
      <div class="tab">COME AND VELORA YOUR BODY</div>
      <div class="figure" style="left:16px;top:40px;width:70px" role="img" aria-label="Illustration: two exercising figures"></div>
      <p>with this class while catching up with friends &amp; meeting new people.<br>It is suitable for all fitness levels.</p>
      <div class="figure" style="right:16px;top:40px;width:70px" role="img" aria-label="Illustration: two exercising figures"></div>
    </div>

    <div class="abs info-box box-strength">
      <div class="tab">IT IS LOW-IMPACT STRENGTH TRAINING</div>
      <div class="figure" style="left:28px;top:58px;width:44px" role="img" aria-label="Illustration: exercising figure"></div>
      <p>with bodyweight exercises to help improve muscular strength,<br>cardiovascular endurance, balance, bone health and functional training.<br>It is suitable for all fitness levels.</p>
      <div class="figure" style="right:28px;top:58px;width:44px" role="img" aria-label="Illustration: exercising figure"></div>
    </div>
  </div>
</body>
</html>
```